Website Design Front page Holistic Members site & Natural Therapist Directory

I need a modern, fresh unique look for a natural therapy and holistic/ Spiritual directory & educational website. It needs to be clear, colourful, inviting and suitable for both sexes - young and old. I want it look fresh and super modern.

I will require the design in .psd format and anything in the centre section including rotational image needs to be supplied in .ai so I can break down the components and colours used will also be needed for frames and banners.

Target Market(s)

all ages, male and female. It must appeal to both therapists and general public.

Requirements
Must have
• Logo obviously. Room for a video player 300 x 250. And small introduction text panel. Must follow the layout in file attached. Also a rotating image up the top, in main section (have supplied example image alter as you like - man pointing top right). Have also supplied example of text to have on it. 16 Menu bars on left frame, under home. Must have 6 prominent links to main pages of site. Have included images use if you want or else use your own. These 6 are, Find a Psychic/ Medium, Find a Natural Therapist, Find a Business/ Club/ School, Find an Event/ Workshop, Find a Product, Holistic Career Centre.I have also attached a shot of the emag, although nothing special in design, useful for complimentary colour choices but not limited to. Another link image/ banner would be Free Chat Now.Another if room and not over crowded would be compare memberships. Can use leader board and leader ad board. Also require the footer to be designed and delivered in .ai similar to lantern vale with link image to quillora and zembly.
Nice to have
• Compare memberships link would be great but not essential... don't want page to look too busy.
Should not have
• Must not be too busy.. think zen with a modern twist.

```html
<!DOCTYPE html>
<html lang="en">
<head>
<meta charset="utf-8">
<title>Soulful Echo – Holistic Community</title>
<link href="https://fonts.googleapis.com/css2?family=Arimo:wght@400;700&display=swap" rel="stylesheet">
<style>
:root{
  --green:#8cc63f;
  --green-dark:#4f7a1c;
  --green-pale:#e6f0d4;
  --purple:#9b2a8e;
  --magenta:#b3309e;
  --orange:#f0913a;
  --blue:#2f8bc4;
  --teal:#2aa3bd;
  --heading:#44609a;
  --ink:#333;
  --ink-soft:#555;
  --panel:#f6f8f0;
  --menu-blue:#c5e6f0;
}
*{margin:0;padding:0;box-sizing:border-box}
html,body{width:1200px;height:900px;overflow:hidden}
body{font-family:"Arimo",Arial,sans-serif;color:var(--ink);position:relative;
  background:linear-gradient(#fff 0,#fff 182px,var(--purple) 182px,var(--purple) 187px,#5e7f24 187px,#7fae32 500px,#8cc63f 900px)}
.abs{position:absolute}

/* header */
.account-tab{left:872px;top:0;width:222px;height:33px;background:var(--green);border-radius:0 0 8px 8px;
  color:#fff;font-size:12.5px;display:flex;align-items:center;justify-content:center;gap:7px}
.brand{left:124px;top:30px;display:flex;align-items:center;gap:10px}
.brand-dot{width:46px;height:46px;border-radius:50%;background:var(--magenta)}
.brand-name{font-size:36px;font-weight:700;color:#2b2b2b;line-height:1}
.contact{right:106px;top:72px;text-align:right;color:#2b2b2b}
.contact small{display:block;font-size:14px}
.contact strong{font-size:19px;letter-spacing:.3px}

/* page frame */
.page{left:103px;top:148px;width:993px;height:760px;background:var(--panel);border:1px solid #a9cf6e;border-radius:9px 9px 0 0}

/* left column */
.search{left:116px;top:188px;width:170px;height:83px;border-radius:6px 6px 0 0;
  background:linear-gradient(#fbe6cf,#f3a45a 60%,#ef8c33)}
.search h3{position:absolute;left:8px;top:10px;font-size:12px;color:#7a3a10;letter-spacing:.3px}
.search .field{position:absolute;left:8px;top:28px;width:145px;height:21px;background:#fff;border:1px solid #4fb6d6}
.search .go{position:absolute;left:11px;top:57px;font-size:11px;font-weight:700;color:#222}
.menu{left:116px;top:272px;width:170px;list-style:none}
.menu li{height:28px;background:var(--green-pale);border-bottom:1px solid #fff;font-size:10px;font-weight:700;
  color:#333;padding-left:12px;display:flex;align-items:center;letter-spacing:.3px}
.menu li.current{background:var(--green);color:#fff;height:27px}
.menu li.signin{background:var(--menu-blue)}
.featured-head{left:116px;top:750px;width:170px;height:29px;background:linear-gradient(#c54fb2,var(--purple));
  color:#fff;font-size:12px;font-weight:700;padding:9px 0 0 11px;border-radius:4px 4px 0 0}
.featured-box{left:116px;top:779px;width:170px;height:130px;background:#fff;border:1px solid var(--purple)}
.featured-photo{left:128px;top:791px;width:148px;height:108px;background:linear-gradient(135deg,#e7e6e3,#cfc6bc);border:4px solid #d8d8d8}

/* hero */
.hero{left:298px;top:191px;width:574px;height:253px;border-radius:6px 6px 0 0;border-bottom:4px solid var(--blue);
  background:linear-gradient(#1f7fc0,#5fb1e0 55%,#dfeef6 78%,#2d82b8 80%,#0f5f99)}
.hero-links{left:637px;top:211px;width:235px;list-style:none}
.hero-links li{height:32px;margin-bottom:4px;background:rgba(168,212,238,.85);border-radius:6px 0 0 6px;
  font-size:12px;font-weight:700;color:#111;padding:10px 0 0 16px}
.hero-links li.active{color:var(--purple)}
.intro-title{left:298px;top:464px;font-size:24px;font-weight:700;color:var(--heading)}
.intro{left:298px;top:508px;width:245px;font-size:11px;line-height:17px;color:#444}
.intro p{margin-bottom:17px}
.video{left:573px;top:512px;width:297px;height:238px;background:#000}
.video-frame{left:573px;top:512px;width:297px;height:208px;background:radial-gradient(circle at 60% 40%,#6b5a42,#2a2018 55%,#0c0a08)}
.video-play{left:698px;top:593px;width:46px;height:46px;border-radius:50%;background:rgba(200,200,200,.55)}
.video-bar{left:573px;top:720px;width:297px;height:30px;background:linear-gradient(#f2f2f2,#cfcfcf);border-top:4px solid #9a9a9a}
.video-bar .time{position:absolute;left:50px;top:9px;font-size:8px;color:#333}
.video-bar .q{position:absolute;left:202px;top:9px;font-size:8px;color:#333}
.thumb{top:783px;width:183px;height:130px;border:3px solid;border-radius:7px}
.thumb.t1{left:298px;border-color:var(--orange);background:linear-gradient(#2b2219,#7a6448)}
.thumb.t2{left:493px;border-color:#7fa83b;background:linear-gradient(#ffffff,#b7d5f0)}
.thumb.t3{left:688px;border-color:var(--teal);background:linear-gradient(#c8b060,#7a5a2a)}

/* right column */
.profile-head{left:884px;top:188px;width:198px;height:30px;background:linear-gradient(#f2f2f2,#cfcfcf);border-radius:5px 5px 0 0;
  font-size:12px;font-weight:700;color:#333;padding:9px 0 0 37px}
.profile-icon{left:896px;top:192px;width:20px;height:22px;border-radius:50% 50% 4px 4px;background:#d13b2c}
.profile-list{left:884px;top:218px;width:198px;height:140px;background:linear-gradient(#fff,#e9e9e9);list-style:none;padding:7px 0 0 18px}
.profile-list li{font-size:10px;line-height:16px;color:#222}
.panel-head{left:884px;width:198px;height:30px;background:linear-gradient(#c54fb2,var(--purple));color:#fff;font-size:12.5px;
  font-weight:700;padding:9px 0 0 42px}
.panel-icon{left:897px;width:21px;height:21px;background:#fff;border-top:5px solid #d8303c;border-radius:2px}
.panel-body{left:884px;width:198px;background:linear-gradient(#fff 50%,#e6f4f8);border:1px solid var(--purple);border-top:0}
.entry{left:904px;width:170px;border-top:1px dotted #3fb0c9;padding-top:8px;font-size:10px;line-height:15px;color:#222}
.entry b{display:block}
.entry b::before{content:"» "}
.entry span{display:block;padding-left:8px}
.more{left:902px;width:86px;height:23px;border-radius:5px;background:linear-gradient(#49bfd9,#1b8aa6);color:#fff;
  font-size:10px;font-weight:700;padding:6px 0 0 8px}
.testimony-head{left:884px;top:833px;width:198px;height:30px;background:linear-gradient(#c54fb2,var(--purple));color:#fff;
  font-size:12.5px;font-weight:700;padding:9px 0 0 42px}
.testimony-icon{left:900px;top:841px;width:20px;height:12px;border-radius:50%;background:#e03a3a}
.testimony-body{left:884px;top:863px;width:198px;height:50px;background:#fff;border:1px solid var(--purple);border-top:0;
  font-size:11px;padding:18px 0 0 23px;color:#111}
</style>
</head>
<body>

<div class="abs account-tab"><span>Contact Us</span>|<span>Sign In</span>|<span>Register</span></div>
<div class="abs brand"><span class="brand-dot"></span><span class="brand-name">Soulful Echo</span></div>
<div class="abs contact"><small>For More Information</small><strong>Call Us: 0100 200 300</strong></div>

<div class="abs page"></div>

<!-- left column -->
<div class="abs search"><h3>COMMUNITY SEARCH</h3><div class="field"></div><div class="go">Search »</div></div>
<ul class="abs menu">
  <li class="current">HOME</li><li>ABOUT US</li><li>LATEST NEWS</li><li>COMMUNITY CALENDAR</li><li>MEMBER SEARCH</li>
  <li class="signin">SIGN IN</li><li>EXCLUSIVE INTERVIEWS</li><li>GUEST PSYCHIC</li><li>FENG SHUI</li><li>YOGA &amp; MEDITATION</li>
  <li>TAROT</li><li>NUMEROLOGY</li><li>CHAKRAS</li><li>BOOK CLUB</li><li>GIVE AWAYS</li><li>HEALTHY RECIPES</li><li>MEMBER SEARCH</li>
</ul>
<div class="abs featured-head">FEATURED MEMBERS</div>
<div class="abs featured-box"></div>
<div class="abs featured-photo" role="img" aria-label="Portrait photo of a featured member"></div>

<!-- centre -->
<div class="abs hero" role="img" aria-label="Rotating banner photo: man in white meditating by the sea, pointing to the top right"></div>
<ul class="abs hero-links">
  <li>FIND A PSYCHIC/ MEDIUM</li><li class="active">FIND A NATURAL THERAPIST</li><li>FIND A BUSINESS/ CLUB/ SCHOOL</li>
  <li>FIND AN EVENT/ WORKSHOP</li><li>FIND A PRODUCT</li><li>HOLISTIC CAREER CENTRE</li>
</ul>
<h1 class="abs intro-title">Lorem Ipsum is simply dummy text</h1>
<div class="abs intro">
  <p>Welcome to <b>Soulful Echo</b> Community &amp; chat rooms. We hope you will explore the various features our sites has to offer. We created this online space for log on and create a dynamic member profile, collaborate on projects, share your ideas and experties - and, most portant, connect with your fellow members.</p>
  <p>Share, collaborate, exchange and grow - that's why we're here and we hope you are too. Engage and explore anytime, from anywhere there's a web connection.</p>
  <p><b>Share. Learn. Grow.</b></p>
</div>
<div class="abs video"></div>
<div class="abs video-frame" role="img" aria-label="Video still: candle, old book and tarot cards"></div>
<div class="abs video-play"><svg width="46" height="46"><path d="M18 14 L32 23 L18 32Z" fill="#fff"/></svg></div>
<div class="abs video-bar">
  <svg class="abs" style="left:5px;top:6px" width="40" height="14"><rect x="2" y="2" width="3" height="10" fill="#333"/><rect x="8" y="2" width="3" height="10" fill="#333"/><path d="M25 5h3l4-3v10l-4-3h-3z" fill="#333"/><path d="M34 4l5 6M39 4l-5 6" stroke="#c22" stroke-width="1.5"/></svg>
  <span class="time">0:00 / 0:32</span><span class="q">360p</span>
  <svg class="abs" style="left:236px;top:5px" width="58" height="16"><rect x="3" y="4" width="10" height="8" fill="none" stroke="#333"/><path d="M24 6h8l-2-2M34 10h-8l2 2" stroke="#333" fill="none"/><path d="M44 3h4M44 3v4M56 3h-4M56 3v4M44 13h4M44 13v-4M56 13h-4M56 13v-4" stroke="#333"/></svg>
</div>
<div class="abs thumb t1" role="img" aria-label="Photo of candle, book and tarot cards"></div>
<div class="abs thumb t2" role="img" aria-label="Photo of a person receiving a head massage"></div>
<div class="abs thumb t3" role="img" aria-label="Photo of a warm-toned spa treatment room"></div>

<!-- right column -->
<div class="abs profile-head">MY PROFILE</div>
<div class="abs profile-icon"></div>
<ul class="abs profile-list">
  <li>» PROFILE HOME</li><li>» MANAGE PROFILE</li><li>» NETWORKS</li><li>» FILES &amp; LINKS</li>
  <li>» FAVORITES</li><li>» MESSAGES</li><li>» CONNECTIONS</li><li>» REFER A FRIEND</li>
</ul>

<div class="abs panel-head" style="top:360px">EVENTS CALENDAR</div>
<div class="abs panel-icon" style="top:364px"></div>
<div class="abs panel-body" style="top:390px;height:140px"></div>
<div class="abs entry" style="top:397px"><b>10/1/2010</b><span>TECH CONF 2010</span></div>
<div class="abs entry" style="top:444px"><b>10/8/2010</b><span>WEB DEV CONF 2010</span></div>
<div class="abs" style="left:904px;top:488px;width:170px;border-top:1px dotted #3fb0c9"></div>
<div class="abs more" style="top:495px">READ MORE ▸</div>

<div class="abs panel-head" style="top:532px">LATEST NEWS</div>
<div class="abs panel-icon" style="top:536px"></div>
<div class="abs panel-body" style="top:562px;height:269px"></div>
<div class="abs entry" style="top:572px"><b>9/16/2010</b><span>Lorem ipsum dolor sit amet</span></div>
<div class="abs entry" style="top:618px"><b>8/26/2010</b><span>Vestibulum id enim vel</span></div>
<div class="abs entry" style="top:664px"><b>9/16/2010</b><span>Integer ac nisi quis felis</span></div>
<div class="abs entry" style="top:712px"><b>8/26/2010</b><span>Pellentesque hendrerit velit ac dolor convallis quis lacinia orci iaculis</span></div>
<div class="abs more" style="top:795px">READ MORE ▸</div>

<div class="abs testimony-head">TESTIMONIALS</div>
<div class="abs testimony-icon"></div>
<div class="abs testimony-body">It's like a Spiritual quillora,</div>

</body>
</html>
```